Painting Contractor Business Card Design

We are looking for a cool, bold, modern, polished, business card design. We are a high-end residential painting contractor. Please incorporate our logo and keep with our green/black color scheme. We are interested in seeing 2-sided and 1-sided options. Thank you very much!

Industry/Entity Type

Business

Contact Information for Business Card

Info for the card:
Owen Talsky
mobile 206-555-0193
email owen@kestrowfinish.net
web www.kestrowfinish.net

```html
<!DOCTYPE html>
<html lang="en">
<head>
<meta charset="utf-8">
<title>Kestrow Finish Business Card</title>
<link rel="stylesheet" href="https://fonts.googleapis.com/css2?family=Lato:wght@400;700&display=swap">
<style>
  :root {
    --page-bg: #e6e6e6;
    --card-black: #050505;
    --text-white: #ffffff;
    --brand-green: #3fae49;
    --band-blue: #1b75bc;
    --band-sky: #27aae1;
    --band-teal: #4cc3b5;
    --band-lime: #8dc63f;
    --band-red: #ef4b2b;
    --band-orange: #f7941d;
    --band-yellow: #fbc52e;
    --band-yellowgreen: #c6d93a;
  }
  * { box-sizing: border-box; margin: 0; padding: 0; }
  html, body { width: 1200px; height: 900px; overflow: hidden; }
  body {
    background: var(--page-bg);
    font-family: "Lato", sans-serif;
    position: relative;
  }
  .card {
    position: absolute;
    left: 260px;
    width: 680px;
    height: 389px;
    background: var(--card-black);
    border-radius: 22px;
    overflow: hidden;
  }
  .card--front { top: 40px; }
  .card--back { top: 471px; }

  .brand {
    display: flex;
    align-items: center;
    gap: 12px;
    color: var(--text-white);
    font-weight: 700;
    font-size: 30px;
    letter-spacing: 1px;
    white-space: nowrap;
  }
  .brand__dot {
    width: 34px; height: 34px;
    border-radius: 50%;
    background: var(--brand-green);
    flex: none;
  }

  .front__row {
    position: absolute;
    left: 0; right: 48px; bottom: 86px;
    display: flex;
    align-items: flex-end;
    gap: 14px;
  }
  .front__line {
    flex: 1;
    height: 3px;
    margin-bottom: 6px;
    background: linear-gradient(90deg, var(--band-yellowgreen), var(--band-yellow) 30%, var(--band-orange) 65%, var(--band-red));
  }

  .back__bands { position: absolute; inset: 0; }
  .back__brand { position: absolute; top: 74px; right: 48px; }

  .contact {
    position: absolute;
    left: 66px;
    bottom: 92px;
    color: var(--text-white);
  }
  .contact__name { font-size: 24px; font-weight: 700; }
  .contact__title { font-size: 17px; color: var(--brand-green); margin-bottom: 8px; }
  .contact__list { list-style: none; }
  .contact__item {
    display: flex; align-items: center; gap: 12px;
    font-size: 16px; line-height: 24px;
  }
  .contact__icon { width: 16px; height: 16px; flex: none; }
</style>
</head>
<body>

<section class="card card--front" aria-label="Card front">
  <div class="front__row">
    <div class="front__line"></div>
    <div class="brand"><span class="brand__dot"></span>KESTROW FINISH</div>
  </div>
</section>

<section class="card card--back" aria-label="Card back">
  <svg class="back__bands" viewBox="0 0 680 389" preserveAspectRatio="none" aria-hidden="true">
    <defs>
      <linearGradient id="topBand" x1="0" x2="1" y1="0" y2="0">
        <stop offset="0" stop-color="var(--band-blue)"/>
        <stop offset="0.45" stop-color="var(--band-sky)"/>
        <stop offset="0.8" stop-color="var(--band-teal)"/>
        <stop offset="1" stop-color="var(--band-lime)"/>
      </linearGradient>
      <linearGradient id="bottomBand" x1="0" x2="1" y1="0" y2="0">
        <stop offset="0" stop-color="var(--band-red)"/>
        <stop offset="0.35" stop-color="var(--band-orange)"/>
        <stop offset="0.7" stop-color="var(--band-yellow)"/>
        <stop offset="1" stop-color="var(--band-lime)"/>
      </linearGradient>
    </defs>
    <polygon points="0,0 680,0 680,10 0,30" fill="url(#topBand)"/>
    <polygon points="0,0 680,0 680,4 0,16" fill="#ffffff" opacity="0.18"/>
    <polygon points="0,362 680,318 680,389 0,389" fill="url(#bottomBand)"/>
    <polygon points="120,389 680,338 680,352 0,389" fill="#ffffff" opacity="0.15"/>
  </svg>

  <div class="brand back__brand"><span class="brand__dot"></span>KESTROW FINISH</div>

  <div class="contact">
    <p class="contact__name">Owen Talsky</p>
    <p class="contact__title">Manager</p>
    <ul class="contact__list">
      <li class="contact__item">
        <svg class="contact__icon" viewBox="0 0 16 16" aria-hidden="true"><path fill="var(--brand-green)" d="M3.5 1.5l2.5 0 1 3.5-1.8 1.2a8 8 0 0 0 4.6 4.6L11 9l3.5 1v2.5a1.5 1.5 0 0 1-1.5 1.5A12 12 0 0 1 2 3a1.5 1.5 0 0 1 1.5-1.5z"/></svg>
        206-555-0193
      </li>
      <li class="contact__item">
        <svg class="contact__icon" viewBox="0 0 16 16" aria-hidden="true"><rect x="1" y="3" width="14" height="10" rx="1" fill="var(--brand-green)"/><path d="M1.5 3.5L8 9l6.5-5.5" fill="none" stroke="#050505" stroke-width="1.3"/></svg>
        owen@kestrowfinish.net
      </li>
      <li class="contact__item">
        <svg class="contact__icon" viewBox="0 0 16 16" aria-hidden="true"><circle cx="8" cy="8" r="7" fill="var(--brand-green)"/><path d="M1 8h14M8 1c-3 3-3 11 0 14M8 1c3 3 3 11 0 14" fill="none" stroke="#050505" stroke-width="1"/></svg>
        www.kestrowfinish.net
      </li>
    </ul>
  </div>
</section>

</body>
</html>
```